study by ripples circle

The website presents a new interactive learning system where it provides not only the teaching material as the instructor friend who can both teach and learn, making friends and making money.
Make friends and get money.

```html
<!DOCTYPE html>
<html lang="en">
<head>
<meta charset="utf-8">
<title>study by ripples circle</title>
<link rel="stylesheet" href="https://fonts.googleapis.com/css2?family=Open+Sans:wght@400;600;700;800&display=swap">
<style>
:root{
  --ink:#2b2b2b;
  --muted:#6f6f6f;
  --rule:#dcdcdc;
  --blue:#2a95d4;
  --blue-dark:#1a6fa6;
  --blue-soft:#e3f0f9;
  --top:#202020;
  --footer:#1c1c1c;
  --white:#ffffff;
}
*{box-sizing:border-box;margin:0;padding:0}
html,body{width:847px;height:1200px;overflow:hidden}
body{font-family:"Open Sans",Arial,sans-serif;color:var(--ink);background:var(--white);font-size:11px;line-height:1.55}
.wrap{width:720px;margin:0 auto;position:relative}

/* header */
.topbar{height:82px;background:var(--top)}
.topbar .wrap{height:82px;display:flex;align-items:center;justify-content:space-between}
.brand{display:flex;align-items:center;gap:10px;color:var(--white);font-weight:800;font-size:28px;letter-spacing:1px}
.brand-dot{width:14px;height:14px;border-radius:50%;background:var(--blue)}
.search{width:150px;height:24px;background:var(--white);font-size:10px;color:#999;padding:0 8px;display:flex;align-items:center}

.nav{height:44px;background:var(--blue)}
.nav .wrap{height:44px;display:flex;align-items:center}
.nav-links{display:flex;gap:52px;list-style:none;padding-left:38px;flex:1}
.nav-links li{color:var(--white);font-size:11px;font-weight:600}
.nav-social{display:flex;height:44px;background:var(--blue-dark);align-items:center;gap:18px;padding:0 22px}
.nav-social span{width:16px;height:16px;border-radius:3px;background:var(--white);opacity:.9}

/* hero */
.hero{height:355px;position:relative;background:linear-gradient(100deg,#8a8f96 0%,#d8dde2 35%,#f2f4f6 55%,#c9cfd6 78%,#9aa2ab 100%)}
.hero-art{position:absolute;inset:0}
.hero-arrow{position:absolute;top:160px;width:22px;height:34px;display:flex;align-items:center;justify-content:center}
.hero-arrow.prev{left:10px}
.hero-arrow.next{right:10px}

/* welcome */
.welcome{padding-top:36px;height:216px;border-bottom:1px solid var(--rule)}
.welcome .wrap{display:flex;justify-content:space-between}
.welcome-text{width:420px}
.section-title{font-size:19px;font-weight:700;color:var(--ink);margin-bottom:12px}
.section-title em{font-style:normal;color:var(--blue)}
.welcome-text p{color:var(--muted);font-size:10.5px}
.video{width:270px;height:148px;position:relative;background:linear-gradient(135deg,#2d3440,#556070 60%,#3a4350)}
.video .play{position:absolute;left:50%;top:50%;transform:translate(-50%,-50%)}

/* services */
.services{padding-top:24px;height:220px}
.services-head{display:flex;justify-content:space-between;align-items:center;margin-bottom:14px}
.services-head .section-title{margin:0}
.arrows{display:flex;gap:6px}
.cards{display:grid;grid-template-columns:repeat(4,1fr);gap:14px}
.card{height:145px;display:flex;flex-direction:column}
.card-art{flex:1}
.card-cap{height:26px;background:var(--blue);color:var(--white);font-size:10.5px;font-weight:600;display:flex;align-items:center;justify-content:center}
.card.feature{background:var(--blue);color:var(--white);text-align:center;padding:22px 14px;align-items:center}
.card.feature h3{font-size:12px;font-weight:700;margin-bottom:6px}
.card.feature p{font-size:9.5px;line-height:1.45;opacity:.9;margin-bottom:10px}
.btn{display:inline-block;background:var(--top);color:var(--white);font-size:9.5px;font-weight:600;padding:4px 12px}

/* lower */
.lower{height:200px;padding-top:10px}
.lower .wrap{display:flex;gap:30px}
.col-title{font-size:13px;font-weight:700;margin-bottom:10px}
.col-title em{font-style:normal;color:var(--blue)}
.news{width:330px}
.post{display:flex;gap:12px;margin-bottom:12px}
.post-date{width:30px;height:34px;border:1px solid var(--rule);text-align:center;font-size:10px;line-height:1.3;padding-top:3px;color:var(--muted);flex-shrink:0}
.post-date b{display:block;color:var(--ink);font-size:11px}
.post h4{font-size:10.5px;font-weight:700}
.post .meta{font-size:9px;color:var(--muted)}
.post p{font-size:9.5px;color:var(--muted);line-height:1.45}
.post p b{color:var(--ink);font-weight:600}
.about{width:180px}
.about h5{font-size:10px;font-weight:600;border-bottom:1px solid var(--rule);padding:4px 0}
.about p{font-size:9.5px;color:var(--muted);padding:6px 0;line-height:1.45}
.contact{flex:1;background:var(--blue-soft)}
.contact-head{background:var(--blue);color:var(--white);font-size:12px;font-weight:700;padding:6px 10px}
.contact-body{padding:6px 10px;font-size:9px;color:var(--muted);line-height:1.4}
.contact-body b{color:var(--blue-dark);font-weight:600;display:block;margin-top:4px}
.contact-body .web{color:var(--blue-dark);margin-top:8px}

/* footer */
.footer{height:93px;background:var(--footer);color:#cfcfcf;border-top:4px solid var(--blue)}
.footer .wrap{display:flex;justify-content:space-between;align-items:flex-start;padding-top:20px}
.footer-links{font-size:9.5px;color:var(--white)}
.footer-copy{font-size:9px;color:#9a9a9a;margin-top:4px}
.footer-social{display:flex;gap:5px}
.footer-social span{width:16px;height:16px;background:var(--blue);border-radius:2px}
.footer-social span:nth-child(even){background:#555}
</style>
</head>
<body>

<header class="topbar">
  <div class="wrap">
    <div class="brand"><span class="brand-dot"></span>RIPPLES</div>
    <div class="search">Search</div>
  </div>
</header>

<nav class="nav">
  <div class="wrap">
    <ul class="nav-links">
      <li>Home</li><li>About Us</li><li>Our Services</li><li>Blog</li><li>Contact Us</li>
    </ul>
    <div class="nav-social"><span></span><span></span><span></span><span></span></div>
  </div>
</nav>

<section class="hero">
  <div class="hero-art" role="img" aria-label="Slider image: a globe surrounded by laptops, tablets, phones and clocks on a grey background, with a young woman holding a pen on the right"></div>
  <div class="hero-arrow prev"><svg width="14" height="24" viewBox="0 0 14 24"><path d="M12 2 3 12l9 10" fill="none" stroke="#fff" stroke-width="3"/></svg></div>
  <div class="hero-arrow next"><svg width="14" height="24" viewBox="0 0 14 24"><path d="M2 2l9 10-9 10" fill="none" stroke="#fff" stroke-width="3"/></svg></div>
</section>

<section class="welcome">
  <div class="wrap">
    <div class="welcome-text">
      <h2 class="section-title">Welcome To <em>Ripples</em></h2>
      <p>Our circle is a new way of learning together. Every member studies with a friendly instructor who teaches and learns at the same time. Share lessons, ask questions and build real friendships while you grow your skills. Join study groups, follow short daily lessons and track your progress in one place. Help others understand a topic and earn rewards for every lesson you share. Learning feels lighter when it moves like ripples across a calm pond.</p>
    </div>
    <div class="video" role="img" aria-label="Video preview of the learning platform">
      <svg class="play" width="40" height="40" viewBox="0 0 40 40"><circle cx="20" cy="20" r="19" fill="#d9322b"/><path d="M16 12v16l12-8z" fill="#fff"/></svg>
    </div>
  </div>
</section>

<section class="services">
  <div class="wrap">
    <div class="services-head">
      <h2 class="section-title">Our <em>Services</em></h2>
      <div class="arrows">
        <svg width="10" height="12" viewBox="0 0 10 12"><path d="M8 1 2 6l6 5" fill="none" stroke="#2b2b2b" stroke-width="2"/></svg>
        <svg width="10" height="12" viewBox="0 0 10 12"><path d="M2 1l6 5-6 5" fill="none" stroke="#2b2b2b" stroke-width="2"/></svg>
      </div>
    </div>
    <div class="cards">
      <div class="card feature">
        <h3>Supernaturalism</h3>
        <p>Learn with a friend who teaches and studies beside you.</p>
        <span class="btn">Read More</span>
      </div>
      <div class="card">
        <div class="card-art" role="img" aria-label="Illustration of people connected around a laptop" style="background:linear-gradient(160deg,#eaf4fb,#b9dcf1)"></div>
        <div class="card-cap">Best Relation Ship</div>
      </div>
      <div class="card">
        <div class="card-art" role="img" aria-label="Photo of a group of smiling friends" style="background:linear-gradient(160deg,#d7dde3,#8e9aa6)"></div>
        <div class="card-cap">Make Friends Get Money</div>
      </div>
      <div class="card">
        <div class="card-art" role="img" aria-label="Photo of a calculator and paperwork on a desk" style="background:linear-gradient(160deg,#f1f1f1,#b8bcc0)"></div>
        <div class="card-cap">Ripple Community</div>
      </div>
    </div>
  </div>
</section>

<section class="lower">
  <div class="wrap">
    <div class="news">
      <h3 class="col-title">Latest News</h3>
      <article class="post">
        <div class="post-date"><b>27</b>Nov</div>
        <div>
          <h4>This is a Standard Post</h4>
          <div class="meta">0 Comment</div>
          <p>Members shared their first group lesson this week and met new study partners from many cities. <b>Read More</b></p>
        </div>
      </article>
      <article class="post">
        <div class="post-date"><b>27</b>Nov</div>
        <div>
          <h4>This is a Standard Post</h4>
          <div class="meta">0 Comment</div>
          <p>A new set of short daily lessons is ready for every circle, with tips from friendly instructors. <b>Read More</b></p>
        </div>
      </article>
    </div>
    <div class="about">
      <h3 class="col-title">More <em>About us</em></h3>
      <h5>Our Mission</h5>
      <h5>Our Team</h5>
      <p>We help people learn, teach and connect in small friendly circles.</p>
      <h5>Our Goals</h5>
    </div>
    <div class="contact">
      <div class="contact-head">Contact Us</div>
      <div class="contact-body">
        <b>Enrollment Office</b>T: +00 1 2345 6701
        <b>Branch Office</b>T: +00 1 2345 6702
        <b>Corporate Office</b>T: +00 1 2345 6703
        <div class="web">www.ripplescircle.example</div>
      </div>
    </div>
  </div>
</section>

<footer class="footer">
  <div class="wrap">
    <div>
      <div class="footer-links">Home | News | Practices | People | Events | Contact | Site Map | Privacy Policy</div>
      <div class="footer-copy">Copyright © 2014 Ripples. All Rights Reserved</div>
    </div>
    <div class="footer-social"><span></span><span></span><span></span><span></span><span></span><span></span></div>
  </div>
</footer>

</body>
</html>
```